Pet store web design

I would like to redesign my current online store (http://brindlecove.example)
I'm looking for a clean, modern design. Any ideas are welcome..

Industry/Entity Type

Pet

Number of Pages Required

3 page

```html
<!DOCTYPE html>
<html lang="en">
<head>
<meta charset="utf-8">
<title>Brindle Cove – Pet Store</title>
<link href="https://fonts.googleapis.com/css2?family=Fredoka:wght@500;600;700&family=Open+Sans:wght@400;600;700&display=swap" rel="stylesheet">
<style>
:root{
  --yellow:#f8e21c;
  --yellow-deep:#f5c400;
  --amber:#f2a300;
  --orange:#f07d10;
  --orange-dark:#d9620a;
  --green:#3aa935;
  --green-light:#7cc84a;
  --blue:#2a8fd8;
  --purple:#8a4fc2;
  --red:#e23a2a;
  --ink:#222;
  --grey:#e4e4e4;
  --grey-mid:#b8b8b8;
  --black:#111;
  --white:#fff;
}
*{box-sizing:border-box;margin:0;padding:0}
html,body{width:843px;height:1200px;overflow:hidden}
body{font-family:"Open Sans",Arial,sans-serif;color:var(--ink);background:var(--white);position:relative}

/* header */
.site-header{position:absolute;left:0;top:0;width:843px;height:128px;background:var(--yellow)}
.brand{position:absolute;left:34px;top:14px;width:210px;height:54px;background:var(--orange);border-radius:10px;display:flex;align-items:center;gap:10px;padding-left:14px}
.brand-dot{width:22px;height:22px;border-radius:50%;background:var(--white)}
.brand-name{font-family:"Fredoka",Arial,sans-serif;font-weight:600;font-size:25px;color:var(--white)}
.contact{position:absolute;top:14px;display:flex;align-items:center;gap:8px;font-size:11px;font-weight:700;color:var(--white)}
.contact .icon{width:26px;height:26px;border-radius:50%;background:var(--orange);display:flex;align-items:center;justify-content:center}
.contact-lines span{display:block;background:var(--orange);padding:1px 6px;border-radius:3px;margin-bottom:3px}
.account-links{position:absolute;left:330px;top:76px;font-size:10px;color:var(--orange-dark)}
.account-links span{margin-right:16px}
.main-nav{position:absolute;left:70px;top:100px;width:700px;height:28px;background:var(--amber);display:flex;align-items:center;justify-content:space-around;font-size:11px;font-weight:600;color:var(--white);border-radius:3px 3px 0 0}
.main-nav .cart{display:flex;align-items:center;gap:6px}

/* hero */
.hero{position:absolute;left:0;top:128px;width:843px;height:266px}
.hero-copy{position:absolute;left:110px;top:68px;width:250px;text-align:center}
.hero-copy h1{font-family:"Fredoka",Arial,sans-serif;font-weight:700;color:var(--orange);font-size:34px;line-height:34px}
.hero-copy p{font-size:13px;line-height:17px;margin-top:6px}
.btn-shop{display:inline-block;margin-top:12px;background:var(--orange);color:var(--white);font-family:"Fredoka",Arial,sans-serif;font-weight:600;font-size:17px;padding:6px 26px;border-radius:4px}
.hero-photo{position:absolute;left:380px;top:10px;width:340px;height:250px;border-radius:6px;background:radial-gradient(circle at 35% 50%,#c98b4a 0,#e9c99a 40%,#f4f1ec 70%)}
.hero-arrow{position:absolute;top:118px;width:16px;height:22px;background:var(--grey-mid);display:flex;align-items:center;justify-content:center}

/* categories */
.categories{position:absolute;left:0;top:394px;width:843px;height:148px;background:var(--grey);display:flex;justify-content:center;gap:18px;padding-top:16px}
.cat{width:95px}
.cat .pic{height:88px}
.cat .label{height:26px;color:var(--white);font-weight:700;font-size:12px;display:flex;align-items:center;justify-content:center}

/* promos */
.promos{position:absolute;left:40px;top:556px;width:770px;height:146px;display:flex;gap:17px}
.promo{flex:1;position:relative;overflow:hidden;background:var(--white);border:1px solid #ddd}
.promo .band{height:72px;background:linear-gradient(135deg,var(--green) 0,var(--green-light) 100%);padding:8px 10px;color:var(--white)}
.promo.orange .band{background:linear-gradient(135deg,var(--orange) 0,var(--yellow-deep) 100%)}
.promo h3{font-family:"Fredoka",Arial,sans-serif;font-size:17px;line-height:18px}
.promo .band p{font-size:8px;line-height:11px;font-weight:600;margin-top:3px}
.promo .pic{position:absolute;left:0;right:0;bottom:0;height:74px}

/* best sellers */
.best{position:absolute;left:40px;top:718px;width:770px}
.best h2{font-family:"Fredoka",Arial,sans-serif;color:var(--orange);font-size:22px;font-weight:600}
.best .pager{position:absolute;right:0;top:8px;font-size:11px;color:var(--grey-mid)}
.products{display:flex;justify-content:space-between;margin-top:10px}
.product{width:140px;text-align:center}
.product .pic{height:70px;margin:0 auto;width:110px;border-radius:4px}
.product .name{font-size:8px;line-height:10px;margin-top:5px;height:20px}
.product .price{font-size:10px;font-weight:700;color:var(--orange-dark)}
.product .add{display:inline-block;margin-top:3px;background:var(--orange);color:var(--white);font-size:8px;padding:2px 10px;border-radius:2px}

/* feature band */
.feature{position:absolute;left:0;top:884px;width:843px;height:132px;background:var(--yellow)}
.info-box{position:absolute;left:56px;width:120px;height:44px;background:var(--white);border-radius:4px;border:2px solid var(--amber);padding:6px 8px;font-size:9px}
.info-box b{display:block;color:var(--orange);font-size:11px}
.feature-photo{position:absolute;left:390px;top:6px;width:410px;height:126px;background:linear-gradient(180deg,#8fd0f2 0,#f2d27a 70%,#e6a640 100%)}

/* footer */
.site-footer{position:absolute;left:0;top:1016px;width:843px;height:184px;background:var(--black);color:var(--white)}
.newsletter{position:absolute;left:40px;top:14px;font-size:11px;font-weight:700}
.signup{position:absolute;left:560px;top:8px;display:flex}
.signup .field{width:160px;height:22px;background:var(--white);border-radius:2px;color:#999;font-size:9px;padding:5px 6px}
.signup .go{width:30px;height:22px;background:var(--blue);margin-left:4px;border-radius:2px}
.footer-cols{position:absolute;left:40px;top:48px;display:flex;gap:34px}
.footer-cols h4{font-size:9px;color:var(--yellow);margin-bottom:4px}
.footer-cols ul{list-style:none}
.footer-cols li{font-size:8px;line-height:12px;color:#ccc}
.footer-brand{position:absolute;left:600px;top:48px}
.footer-brand .brand-name{font-size:22px;color:var(--yellow)}
.payments{display:flex;gap:5px;margin-top:12px}
.payments span{width:32px;height:20px;background:#555;border-radius:2px}
.copyright{position:absolute;left:0;bottom:8px;width:843px;text-align:center;font-size:8px;color:#888}
</style>
</head>
<body>

<header class="site-header">
  <div class="brand"><span class="brand-dot"></span><span class="brand-name">Brindle Cove</span></div>

  <div class="contact" style="left:290px">
    <span class="icon"><svg width="14" height="14" viewBox="0 0 24 24"><path fill="#fff" d="M6.6 10.8a15 15 0 0 0 6.6 6.6l2.2-2.2c.3-.3.7-.4 1-.2 1.1.4 2.3.6 3.6.6.6 0 1 .4 1 1V20c0 .6-.4 1-1 1A17 17 0 0 1 3 4c0-.6.4-1 1-1h3.5c.6 0 1 .4 1 1 0 1.3.2 2.5.6 3.6.1.3 0 .7-.2 1z"/></svg></span>
    <div class="contact-lines"><span>(555) 014-2288</span><span>hello@brindlecove.example</span></div>
  </div>

  <div class="contact" style="left:520px">
    <span class="icon"><svg width="14" height="14" viewBox="0 0 24 24"><path fill="#fff" d="M6.6 10.8a15 15 0 0 0 6.6 6.6l2.2-2.2c.3-.3.7-.4 1-.2 1.1.4 2.3.6 3.6.6.6 0 1 .4 1 1V20c0 .6-.4 1-1 1A17 17 0 0 1 3 4c0-.6.4-1 1-1h3.5c.6 0 1 .4 1 1 0 1.3.2 2.5.6 3.6.1.3 0 .7-.2 1z"/></svg></span>
    <div class="contact-lines"><span>24 hr phone:</span><span>(555) 014-2299</span></div>
  </div>

  <div class="account-links"><span>Register</span><span>Sign In</span></div>

  <nav class="main-nav">
    <span>My Account</span><span>My Cart</span><span>Checkout</span><span>My Wishlist</span><span>Log In</span>
    <span class="cart"><svg width="14" height="12" viewBox="0 0 24 20"><path d="M0 1h4l3 11h12l3-8H7" stroke="#fff" stroke-width="2" fill="none"/><circle cx="9" cy="17" r="2" fill="#fff"/><circle cx="18" cy="17" r="2" fill="#fff"/></svg>0 items</span>
  </nav>
</header>

<section class="hero">
  <span class="hero-arrow" style="left:4px"><svg width="8" height="10"><path d="M7 0 1 5l6 5z" fill="#fff"/></svg></span>
  <div class="hero-copy">
    <h1>BRINDLE<br>COVE</h1>
    <p>We've got it all,<br>for the big the medium and the small</p>
    <span class="btn-shop">Shop Now</span>
  </div>
  <div class="hero-photo" role="img" aria-label="Photo of a puppy and a white kitten sitting side by side"></div>
  <span class="hero-arrow" style="right:4px"><svg width="8" height="10"><path d="M1 0l6 5-6 5z" fill="#fff"/></svg></span>
</section>

<section class="categories">
  <div class="cat"><div class="pic" role="img" aria-label="Photo of colourful parrots" style="background:linear-gradient(160deg,#3fa34d,#f2c531)"></div><div class="label" style="background:var(--blue)">Birds</div></div>
  <div class="cat"><div class="pic" role="img" aria-label="Photo of a kitten" style="background:linear-gradient(160deg,#c9a06a,#f0e0c4)"></div><div class="label" style="background:var(--orange)">Cats</div></div>
  <div class="cat"><div class="pic" role="img" aria-label="Photo of a dog on orange" style="background:linear-gradient(160deg,#f39b1d,#c7792e)"></div><div class="label" style="background:var(--orange-dark)">Dogs</div></div>
  <div class="cat"><div class="pic" role="img" aria-label="Photo of a goldfish" style="background:linear-gradient(160deg,#1e7fd0,#f28a1a)"></div><div class="label" style="background:var(--blue)">Fish</div></div>
  <div class="cat"><div class="pic" role="img" aria-label="Photo of a rabbit" style="background:linear-gradient(160deg,#8a4fc2,#d9c7a6)"></div><div class="label" style="background:var(--purple)">Small Pets</div></div>
  <div class="cat"><div class="pic" role="img" aria-label="Photo of a person walking a dog outdoors" style="background:linear-gradient(160deg,#f4f4f4,#cfd8c4)"></div><div class="label" style="background:var(--red)">Out door</div></div>
</section>

<section class="promos">
  <div class="promo">
    <div class="band"><h3>FALL / WINTER</h3><p>Too Fast For Human Eye!<br>Jumpsuit High Grade 100%<br>Cotton Dog Racing Uniforms</p></div>
    <div class="pic" role="img" aria-label="Photo of red dog racing jumpsuits" style="background:linear-gradient(180deg,#fff,#d8312a)"></div>
  </div>
  <div class="promo">
    <div class="band"><h3>FALL / WINTER</h3><p>Show em Who's boss!<br>Jumpsuit Graphic Design<br>100% Cotton Dark Blue Color</p></div>
    <div class="pic" role="img" aria-label="Photo of navy police style dog jumpsuits" style="background:linear-gradient(180deg,#fff,#1d2a55)"></div>
  </div>
  <div class="promo orange">
    <div class="band"><h3>FALL / WINTER</h3><p>Warm the cold winter<br>Coats for every size of dog</p></div>
    <div class="pic" role="img" aria-label="Photo of a dog in a camouflage winter coat" style="background:linear-gradient(180deg,#fff,#7d7350)"></div>
  </div>
</section>

<section class="best">
  <h2>Best Sellers</h2>
  <span class="pager">‹ ›</span>
  <div class="products">
    <div class="product"><div class="pic" role="img" aria-label="Photo of a dog in a shirt costume" style="background:linear-gradient(#f2f2f2,#c9cfd8)"></div><div class="name">Shirt Dog Costume - Large</div><div class="price">$39.00</div><span class="add">Add to Cart</span></div>
    <div class="product"><div class="pic" role="img" aria-label="Photo of a dog in a holiday costume" style="background:linear-gradient(#f2f2f2,#b84a3a)"></div><div class="name">Holiday Tree Shirt Dog Costume - Extra Small</div><div class="price">$35.00</div><span class="add">Add to Cart</span></div>
    <div class="product"><div class="pic" role="img" aria-label="Photo of a round pet nest bed" style="background:linear-gradient(#f2f2f2,#8a7a5c)"></div><div class="name">Nest Bed - Large Loft Hammock</div><div class="price">$299.00</div><span class="add">Add to Cart</span></div>
    <div class="product"><div class="pic" role="img" aria-label="Photo of a small pet tent" style="background:linear-gradient(#f2f2f2,#5c6a48)"></div><div class="name">Cozy Den Tent - Large</div><div class="price">$79.00</div><span class="add">Add to Cart</span></div>
    <div class="product"><div class="pic" role="img" aria-label="Photo of a red pet treadmill" style="background:linear-gradient(#f2f2f2,#c62a22)"></div><div class="name">Stride Pet Treadmill</div><div class="price">$899.00</div><span class="add">Add to Cart</span></div>
  </div>
</section>

<section class="feature">
  <div class="info-box" style="top:22px"><b>Free Delivery</b>On orders over $50</div>
  <div class="info-box" style="top:74px"><b>Easy Returns</b>Within 30 days</div>
  <div class="feature-photo" role="img" aria-label="Photo of a dog wearing goggles racing outdoors"></div>
</section>

<footer class="site-footer">
  <p class="newsletter">Keep up to date on the latest from brindlecove.example. We care.</p>
  <div class="signup"><span class="field">Enter your email</span><span class="go"></span></div>
  <div class="footer-cols">
    <div><h4>Quick Links</h4><ul><li>Home</li><li>About Us</li><li>Shop</li><li>Contact</li></ul></div>
    <div><h4>Services</h4><ul><li>Delivery</li><li>Returns</li><li>Gift Cards</li><li>Grooming</li></ul></div>
    <div><h4>Information</h4><ul><li>Privacy Policy</li><li>Terms of Use</li><li>Site Map</li><li>FAQ</li></ul></div>
    <div><h4>About Us</h4><ul><li>Our Story</li><li>Careers</li><li>Blog</li><li>Reviews</li></ul></div>
  </div>
  <div class="footer-brand">
    <span class="brand-name">Brindle Cove</span>
    <div class="payments"><span></span><span></span><span></span><span></span></div>
  </div>
  <p class="copyright">© Brindle Cove. All rights reserved.</p>
</footer>

</body>
</html>
```